Business Card Design

The business card is for an IT services company with a specialism
in Integration Services Markets are Health, Government and finance, we provide Velmora SOA platforms and CWR Trellis integration. We are developing multi-agency connectivity

Industry/Entity Type

Business

Contact Information for Business Card

Martin Gorse
Director

BQVo Ltd Martin.gorse@bqvoltd.co.uk

Mobile: +44 (0) 7700900418
Tel: +44 (0) 1632 960583
Website: www.bqvoltd.co.uk

Fenwright House, Fenwright Square, Dunmere ZX98 4QT

Percival Hanley
Health Integration Services

Mobile +44 (0) 07700900276
Tel +44 (0) 1632 960583
Address as above

```html
<!DOCTYPE html>
<html lang="en">
<head>
<meta charset="utf-8">
<title>Martin Gorse – Business Card</title>
<link rel="stylesheet" href="https://fonts.googleapis.com/css2?family=Montserrat:ital,wght@0,300;0,700;1,400&family=Didact+Gothic&display=swap">
<style>
  :root {
    --bright-blue: #3a78f5;
    --deep-blue: #2152cc;
    --ink: #111111;
    --slate: #555555;
    --muted: #444444;
    --contact-text: #d4e0ff;
    --paper: #ffffff;
  }
  html, body {
    margin: 0;
    padding: 0;
    overflow: hidden;
    background: var(--paper);
  }
  .card {
    position: relative;
    width: 791px;
    height: 1200px;
    overflow: hidden;
    background: var(--paper);
    font-family: "Didact Gothic", "Century Gothic", sans-serif;
  }
  .top-bar {
    position: absolute;
    left: 0; top: 0;
    width: 100%; height: 46px;
    background: var(--bright-blue);
  }
  .name {
    position: absolute;
    left: 0; top: 293px;
    width: 100%;
    margin: 0;
    text-align: center;
    font-family: "Montserrat", "Century Gothic", sans-serif;
    font-size: 79px;
    line-height: 1;
    letter-spacing: -2px;
  }
  .name .first { font-weight: 700; color: var(--ink); }
  .name .last { font-weight: 300; color: var(--slate); }
  .name-shadow {
    position: absolute;
    left: 110px; top: 380px;
    width: 595px; height: 14px;
  }
  .role {
    position: absolute;
    left: 0; top: 394px;
    width: 100%;
    margin: 0;
    text-align: center;
    font-family: "Montserrat", "Century Gothic", sans-serif;
    font-style: italic;
    font-weight: 400;
    font-size: 27px;
    color: var(--muted);
    letter-spacing: -0.5px;
  }
  .dome {
    position: absolute;
    left: 0; top: 0;
    width: 791px; height: 1200px;
  }
  .band {
    position: absolute;
    left: 0;
    width: 100%;
  }
  .band--address { top: 650px; height: 187px; background: var(--deep-blue); }
  .band--web { top: 837px; height: 187px; background: var(--bright-blue); }
  .band--phone { top: 1024px; height: 176px; background: var(--deep-blue); }
  .icon {
    position: absolute;
  }
  .contact-text {
    position: absolute;
    margin: 0;
    color: var(--contact-text);
    font-size: 26px;
    line-height: 33px;
    white-space: nowrap;
  }
</style>
</head>
<body>
<main class="card">
  <div class="top-bar"></div>

  <h1 class="name"><span class="first">MARTIN</span> <span class="last">GORSE</span></h1>
  <svg class="name-shadow" viewBox="0 0 595 14" aria-hidden="true">
    <defs>
      <linearGradient id="shadowFade" x1="0" x2="1">
        <stop offset="0" stop-color="#000" stop-opacity="0.15"/>
        <stop offset="0.5" stop-color="#000" stop-opacity="0.85"/>
        <stop offset="1" stop-color="#000" stop-opacity="0.15"/>
      </linearGradient>
    </defs>
    <path d="M0 4 Q297 -2 595 4 Q297 14 0 4 Z" fill="url(#shadowFade)"/>
  </svg>
  <p class="role">DIRECTOR BQVO LTD</p>

  <svg class="dome" viewBox="0 0 791 1200" aria-hidden="true">
    <circle cx="394" cy="792" r="316" fill="var(--deep-blue)"/>
  </svg>

  <section class="band band--address">
    <svg class="icon" style="left:102px;top:49px" width="56" height="89" viewBox="0 0 56 89" aria-hidden="true">
      <path d="M28 2 C13 2 2 13 2 28 C2 45 20 62 28 87 C36 62 54 45 54 28 C54 13 43 2 28 2 Z" fill="#fff" stroke="#222" stroke-width="2"/>
      <circle cx="28" cy="27" r="13" fill="var(--deep-blue)" stroke="#222" stroke-width="2"/>
    </svg>
    <p class="contact-text" style="left:217px;top:62px">Fenwright House, Fenwright Square,<br>Dunmere ZX98 4QT</p>
  </section>

  <section class="band band--web">
    <svg class="icon" style="left:83px;top:48px" width="92" height="92" viewBox="0 0 92 92" aria-hidden="true">
      <circle cx="46" cy="46" r="44" fill="#fff" stroke="#222" stroke-width="2"/>
      <g fill="none" stroke="#222" stroke-width="4">
        <circle cx="46" cy="46" r="34"/>
        <ellipse cx="46" cy="46" rx="15" ry="34"/>
        <line x1="46" y1="12" x2="46" y2="80"/>
        <line x1="12" y1="46" x2="80" y2="46"/>
        <line x1="17" y1="30" x2="75" y2="30"/>
        <line x1="17" y1="62" x2="75" y2="62"/>
      </g>
    </svg>
    <p class="contact-text" style="left:222px;top:78px">www.bqvoltd.co.uk</p>
  </section>

  <section class="band band--phone">
    <svg class="icon" style="left:84px;top:57px" width="92" height="72" viewBox="0 0 92 72" aria-hidden="true">
      <g fill="#fff" stroke="#222" stroke-width="2" stroke-linejoin="round">
        <path d="M4 14 C4 4 88 4 88 14 L88 22 L70 24 L68 15 C58 12 34 12 24 15 L22 24 L4 22 Z"/>
        <path d="M30 18 L62 18 L64 28 L84 52 L84 70 L8 70 L8 52 L28 28 Z"/>
      </g>
      <g fill="#222">
        <rect x="36" y="38" width="5" height="5"/><rect x="44" y="38" width="5" height="5"/><rect x="52" y="38" width="5" height="5"/>
        <rect x="36" y="46" width="5" height="5"/><rect x="44" y="46" width="5" height="5"/><rect x="52" y="46" width="5" height="5"/>
        <rect x="36" y="54" width="5" height="5"/><rect x="44" y="54" width="5" height="5"/><rect x="52" y="54" width="5" height="5"/>
      </g>
    </svg>
    <p class="contact-text" style="left:217px;top:69px">+44 (0) 7700900418<br>+44 (0) 1632 960583</p>
  </section>
</main>
</body>
</html>
```